A modern, fresh introduction to Buddhism

I need a book cover for an A6 sized book to be used both for ebook and hard copy. The author is a young, modern Buddhist teacher of high standing who has written this short intro to Buddhism in an informal Q & As format using modern, accessible language to convey profound and meaningful ideas to the general public. The author is Tibetan, but teaches worldwide and is very personable and dynamic. The cover should portray this and have a fresh yet authentic feel to it (nothing new-agey!). Please see the author's websites www.norvalemtasheteacher.org and www.pwrt.org for reference, but do not feel that the design must align completely with the website designs.

Target Market(s)

General public both in Europe and America and in Asia ranging from teenagers to the elderly. A really broad audience.

Industry/Entity Type

Teacher

Requirements
Must have
• Please include the following text that on the front cover:

A Window onto Stillness

By Drawa Tsomen Lhundrup

Please include the following on the back cover:

Yunor Trenpa Publications (with attached logo above it)
Nice to have
• A simplistic, artistic, and modern look without any traditional religious images.
Should not have
• No buddha images or religious images. I would prefer a more simplistic, modern and artistic look.

```html
<!DOCTYPE html>
<html lang="en">
<head>
<meta charset="utf-8">
<title>A Window onto Stillness — Cover</title>
<link rel="stylesheet" href="https://fonts.googleapis.com/css2?family=Inter+Tight:wght@300;400&family=EB+Garamond:ital,wght@1,600&display=swap">
<style>
  :root {
    --backdrop: #1f1c1a;
    --cover: #ffffff;
    --ink: #1a1a1a;
    --ink-soft: #8a8a8a;
    --accent: #d81f7d;
    --petal-light: #fbd3e0;
    --petal-deep: #ee7fa6;
  }
  * { margin: 0; padding: 0; box-sizing: border-box; }
  html, body {
    width: 1200px;
    height: 1000px;
    overflow: hidden;
    background: var(--backdrop);
  }
  .cover {
    position: absolute;
    left: 350px;
    top: 148px;
    width: 500px;
    height: 704px;
    background: var(--cover);
  }
  .flower-art {
    position: absolute;
    left: 174px;
    top: 106px;
    width: 172px;
    height: 98px;
  }
  .title {
    position: absolute;
    left: 82px;
    top: 278px;
    font-family: "Inter Tight", "Helvetica Neue", Arial, sans-serif;
    color: var(--ink);
  }
  .title-lead {
    display: block;
    font-size: 15px;
    font-weight: 400;
    letter-spacing: 0.2px;
    color: var(--ink-soft);
    line-height: 1;
    margin-bottom: -14px;
  }
  .title-main {
    display: block;
    font-size: 128px;
    font-weight: 300;
    letter-spacing: -4px;
    line-height: 78px;
    padding-top: 18px;
  }
  .subtitle {
    position: absolute;
    left: 82px;
    width: 344px;
    top: 468px;
    text-align: center;
    font-family: "EB Garamond", Georgia, serif;
    font-style: italic;
    font-weight: 600;
    font-size: 17.5px;
    white-space: nowrap;
    color: var(--accent);
  }
  .author {
    position: absolute;
    left: 0;
    width: 100%;
    top: 566px;
    text-align: center;
    font-family: "Inter Tight", "Helvetica Neue", Arial, sans-serif;
    font-weight: 300;
    font-size: 30px;
    line-height: 40px;
    color: var(--ink);
    text-transform: uppercase;
  }
</style>
</head>
<body>
  <main class="cover">
    <svg class="flower-art" viewBox="0 0 172 98" role="img" aria-label="Illustration of a single pink lotus flower on a long green stem">
      <defs>
        <radialGradient id="petalTone" cx="50%" cy="55%" r="60%">
          <stop offset="0%" stop-color="var(--petal-light)"/>
          <stop offset="100%" stop-color="var(--petal-deep)"/>
        </radialGradient>
      </defs>
      <ellipse cx="86" cy="52" rx="85" ry="44" fill="url(#petalTone)"/>
    </svg>

    <h1 class="title">
      <span class="title-lead">A WINDOW ONTO</span>
      <span class="title-main">still<br>ness</span>
    </h1>

    <p class="subtitle">A Short Companion to a Calm and Clear Mind</p>

    <p class="author">Drawa Tsomen<br>Lhundrup</p>
  </main>
</body>
</html>
```